Online-Marketing Material für Recruiting-Plattform
Zielgruppe
Recruiting-Plattform für Physiotherapeuten. Wir sind Vermittler.
Aufgabenstellung
Ich benötige ein 2er Set aus Social-Media-Templates, das wir als Basis für Recruiting-Ads nutzen können.
Variante 1: (1080 x 1350) mit jeweils 285 Pixel Safe Space oben und unten (hier keine wichtigen Elemente).
Wichtig: Es handelt sich um ein Template. Daher muss es mit verschiedenen Elementen und Fotos funktionieren.
Die Elemente werden später durch variable Inhalte gesetzt. Ziel ist es, ein möglichst flexibles Format zu schaffen,
das mit unterschiedlichen Inhalten funktioniert.
Bitte orientiere dich am Grunddesign der Website kurapunkt.de
Elemente und zugehörige Beispiele sind
1. Foto in querformat | Beispiel als Download)
2. Jobtitel als Headline | (Physiotherapeut (m/w/d)
3. Subtitle | Werde Teil eines wachsenden Teams
4. Arbeitszeitmodell | Vollzeit, Teilzeit
3. Ort | Hannover
4. 3 x Highlights | 1. Betriebliche Krankenversicherung 2. Pedalo 3. Gehalt bis zu 4.500 EUR
(Die Highlight variieren thematisch, daher hier bitte nur mit thematisch-neutralen Icons arbeiten.
5. Logo des Arbeitgebers (velmo) auf weiß
Variante 2 mit Foto in hochformat

```html
<!DOCTYPE html>
<html lang="en">
<head>
<meta charset="utf-8">
<title>Recruiting Ad – Physiotherapist</title>
<link rel="stylesheet" href="https://fonts.googleapis.com/css2?family=Jost:ital,wght@0,400;0,500;0,600;1,400&display=swap">
<style>
  :root {
    --pink: #d5547b;
    --blue: #5b92c3;
    --text-blue: #5a8fc4;
    --ink: #1f3a44;
    --white: #ffffff;
  }
  html, body {
    margin: 0;
    padding: 0;
    overflow: hidden;
    background: var(--white);
  }
  .ad {
    position: relative;
    width: 960px;
    height: 1200px;
    overflow: hidden;
    background: var(--white);
    font-family: "Jost", sans-serif;
  }
  .accent {
    position: absolute;
    border-radius: 50%;
  }
  .accent--top-main { width: 260px; height: 260px; right: -110px; top: -70px; background: var(--pink); }
  .accent--top-small { width: 130px; height: 130px; right: -50px; top: 250px; background: var(--blue); }
  .accent--bottom-main { width: 240px; height: 240px; left: -110px; bottom: -90px; background: var(--blue); }
  .accent--bottom-small { width: 150px; height: 150px; left: 170px; bottom: -80px; background: var(--pink); }
  .job-photo {
    position: absolute;
    left: 162px;
    top: 253px;
    width: 366px;
    height: 205px;
    border-radius: 14px;
    background: linear-gradient(120deg, #e9eef2 0%, #dfe4e8 40%, #c9d2da 60%, #f2f2f0 100%);
  }
  .headline {
    position: absolute;
    left: 160px;
    top: 540px;
    margin: 0;
    font-size: 34px;
    font-weight: 600;
    color: var(--text-blue);
    white-space: nowrap;
  }
  .headline .lead { color: var(--pink); }
  .subtitle {
    position: absolute;
    left: 160px;
    top: 598px;
    margin: 0;
    font-size: 22px;
    font-style: italic;
    letter-spacing: 0.9px;
    color: var(--text-blue);
    white-space: nowrap;
  }
  .facts { position: absolute; top: 708px; }
  .fact {
    position: absolute;
    top: 0;
    text-align: center;
    color: var(--text-blue);
    font-size: 22px;
    font-weight: 500;
    letter-spacing: 0.6px;
    white-space: nowrap;
  }
  .fact svg { display: block; margin: 0 auto 12px; }
  .fact--time { left: 160px; width: 88px; }
  .fact--place { left: 290px; width: 84px; }
  .highlights {
    position: absolute;
    left: 476px;
    top: 713px;
    margin: 0;
    padding: 0;
    list-style: none;
  }
  .highlight {
    display: flex;
    align-items: center;
    height: 32px;
    margin-bottom: 30px;
    color: var(--text-blue);
    font-size: 17.5px;
    font-weight: 500;
    letter-spacing: 0.5px;
    white-space: nowrap;
  }
  .highlight svg { flex: none; margin-right: 14px; }
  .employer {
    position: absolute;
    left: 676px;
    top: 928px;
    display: flex;
    align-items: center;
    gap: 8px;
    color: var(--ink);
    font-size: 34px;
    font-weight: 400;
  }
  .employer .dot {
    width: 16px;
    height: 16px;
    border-radius: 50%;
    background: var(--ink);
  }
</style>
</head>
<body>
<main class="ad">
  <div class="accent accent--top-main" aria-hidden="true"></div>
  <div class="accent accent--top-small" aria-hidden="true"></div>
  <div class="accent accent--bottom-main" aria-hidden="true"></div>
  <div class="accent accent--bottom-small" aria-hidden="true"></div>

  <div class="job-photo" role="img" aria-label="Landscape photo: a physiotherapist stretching the leg of a patient lying on a treatment bench in a bright practice room"></div>

  <h1 class="headline"><span class="lead">Looking for:</span> Physiotherapist (m/f/d)</h1>
  <p class="subtitle">Become part of a growing team</p>

  <div class="facts">
    <div class="fact fact--time">
      <svg width="54" height="56" viewBox="0 0 54 56" aria-hidden="true">
        <rect x="6" y="4" width="20" height="8" rx="2" fill="none" stroke="var(--pink)" stroke-width="3"/>
        <rect x="2" y="11" width="46" height="34" rx="4" fill="var(--pink)"/>
        <rect x="2" y="24" width="46" height="3" fill="var(--white)"/>
        <rect x="20" y="20" width="8" height="10" rx="1" fill="var(--white)"/>
        <circle cx="40" cy="42" r="12" fill="var(--white)" stroke="var(--pink)" stroke-width="3"/>
        <path d="M 40 35 V 42 H 46" fill="none" stroke="var(--pink)" stroke-width="2.5" stroke-linecap="round"/>
      </svg>
      Full-time
    </div>
    <div class="fact fact--place">
      <svg width="58" height="56" viewBox="0 0 58 56" aria-hidden="true">
        <circle cx="25" cy="31" r="24" fill="var(--pink)"/>
        <path d="M 40 2 C 31 2 27 9 29 16 C 31 22 40 32 40 32 C 40 32 49 22 51 16 C 53 9 49 2 40 2 Z" fill="var(--white)" stroke="var(--pink)" stroke-width="3" stroke-linejoin="round"/>
      </svg>
      Hanover
    </div>
  </div>

  <ul class="highlights">
    <li class="highlight">
      <svg width="32" height="32" viewBox="0 0 32 32" aria-hidden="true"><circle cx="16" cy="16" r="16" fill="var(--pink)"/><path d="M16 8v16M8 16h16" stroke="var(--white)" stroke-width="4"/></svg>
      Betriebliche Krankenversicherung
    </li>
    <li class="highlight">
      <svg width="32" height="32" viewBox="0 0 32 32" aria-hidden="true"><circle cx="16" cy="16" r="16" fill="var(--pink)"/><path d="M16 8v16M8 16h16" stroke="var(--white)" stroke-width="4"/></svg>
      Pedalo
    </li>
    <li class="highlight">
      <svg width="32" height="32" viewBox="0 0 32 32" aria-hidden="true"><circle cx="16" cy="16" r="16" fill="var(--pink)"/><path d="M16 8v16M8 16h16" stroke="var(--white)" stroke-width="4"/></svg>
      Gehalt bis zu 4.500 EUR
    </li>
  </ul>

  <div class="employer">
    <span class="name">velmo</span>
    <span class="dot" aria-hidden="true"></span>
  </div>
</main>
</body>
</html>
```